Breezeway Masters Business Card Design

Design new, 2 sides, business cards for a residential and light commercial heating, air conditioning contractor.

Target Market(s)

Homeowners, small businesses

Industry/Entity Type

Business

Contact Information for Business Card

Dominic Halvorsen
Phone - 862-415-2763
Email
Address - PO box 648
Brookvale NJ 07412
Website - www.BreezewayMastersLLC.example

Requirements
Must have
• logo, company colors, standard size with no die cut, so I can use nimbo press

```html
<!DOCTYPE html>
<html lang="en">
<head>
<meta charset="utf-8">
<title>Breezeway Masters Business Card</title>
<link rel="stylesheet" href="https://fonts.googleapis.com/css2?family=Josefin+Sans:wght@400;600;700&display=swap">
<style>
  :root {
    --crimson: #c2304c;
    --crimson-deep: #a7213e;
    --gold: #eeb543;
    --orange: #e48a24;
    --cream: #fbeed2;
    --ink: #3a2413;
    --white: #ffffff;
    --backdrop: #e9e2d6;
  }
  * { margin: 0; padding: 0; box-sizing: border-box; }
  html, body { width: 1200px; height: 1023px; overflow: hidden; }
  body {
    background: var(--backdrop);
    font-family: "Josefin Sans", sans-serif;
    position: relative;
  }
  .card {
    position: absolute;
    left: 220px;
    width: 760px;
    height: 434px;
    border-radius: 18px;
    overflow: hidden;
    box-shadow: 0 10px 28px rgba(60, 35, 20, 0.25);
  }
  .card--front { top: 48px; background: linear-gradient(135deg, var(--crimson), var(--crimson-deep)); }
  .card--back { top: 540px; background: linear-gradient(135deg, var(--crimson), var(--crimson-deep)); }

  .front-brand {
    position: absolute;
    left: 0; right: 0; top: 0; bottom: 62px;
    display: flex; align-items: center; justify-content: center; gap: 18px;
  }
  .brand-name {
    color: var(--cream);
    font-weight: 700;
    text-transform: uppercase;
    letter-spacing: 3px;
    white-space: nowrap;
  }
  .front-brand .brand-name { font-size: 50px; }
  .brand-dot { width: 22px; height: 22px; border-radius: 50%; background: var(--gold); flex: none; }
  .front-band {
    position: absolute; left: 0; right: 0; bottom: 0; height: 62px;
    background: linear-gradient(90deg, var(--gold), var(--orange));
    display: flex; align-items: center; justify-content: center;
    color: var(--ink); font-size: 18px; letter-spacing: 1.5px;
  }

  .back-brand {
    position: absolute; right: 40px; top: 36px;
    display: flex; align-items: center; gap: 10px;
  }
  .back-brand .brand-name { font-size: 24px; letter-spacing: 2px; }
  .back-brand .brand-dot { width: 12px; height: 12px; }
  .person {
    position: absolute; right: 40px; top: 150px; text-align: right;
  }
  .person-name { color: var(--white); font-weight: 700; font-size: 30px; letter-spacing: 1px; }
  .person-title { color: var(--cream); font-size: 15px; margin-top: 6px; letter-spacing: 1px; }
  .back-band {
    position: absolute; left: 0; right: 0; bottom: 0; height: 168px;
    background: linear-gradient(90deg, var(--orange), var(--gold));
    border-top: 4px solid var(--white);
    padding: 22px 40px;
  }
  .contact-list { list-style: none; }
  .contact-list li {
    display: flex; align-items: center; gap: 12px;
    color: var(--ink); font-size: 17px; letter-spacing: 1px; line-height: 30px;
    white-space: nowrap;
  }
  .contact-list svg { width: 16px; height: 16px; flex: none; }
</style>
</head>
<body>
  <section class="card card--front" aria-label="Card front">
    <div class="front-brand">
      <span class="brand-dot"></span>
      <span class="brand-name">Breezeway Masters</span>
    </div>
    <div class="front-band">www.BreezewayMastersLLC.example</div>
  </section>

  <section class="card card--back" aria-label="Card back">
    <div class="back-brand">
      <span class="brand-dot"></span>
      <span class="brand-name">Breezeway Masters</span>
    </div>
    <div class="person">
      <div class="person-name">Dominic Halvorsen</div>
      <div class="person-title">Title</div>
    </div>
    <div class="back-band">
      <ul class="contact-list">
        <li>
          <svg viewBox="0 0 16 16"><circle cx="8" cy="8" r="8" fill="var(--crimson)"/><path d="M5 4.5l1.6-.5 1 2-1 .8a5 5 0 0 0 2.6 2.6l.8-1 2 1-.5 1.6c-3.5.2-6.7-3-6.5-6.5z" fill="var(--cream)"/></svg>
          862-415-2763
        </li>
        <li>
          <svg viewBox="0 0 16 16"><rect x="1" y="3" width="14" height="10" rx="1" fill="none" stroke="var(--crimson)" stroke-width="1.5"/><path d="M1.5 4l6.5 5 6.5-5" fill="none" stroke="var(--crimson)" stroke-width="1.5"/></svg>
          info@breezewaymastersllc.example
        </li>
        <li>
          <svg viewBox="0 0 16 16"><circle cx="8" cy="8" r="6.5" fill="none" stroke="var(--crimson)" stroke-width="1.5"/><ellipse cx="8" cy="8" rx="3" ry="6.5" fill="none" stroke="var(--crimson)" stroke-width="1.2"/><path d="M1.5 8h13" stroke="var(--crimson)" stroke-width="1.2"/></svg>
          www.breezewaymastersllc.example
        </li>
        <li>
          <svg viewBox="0 0 16 16"><path d="M8 15s5-5.2 5-8.5A5 5 0 0 0 3 6.5C3 9.8 8 15 8 15z" fill="var(--crimson)"/><circle cx="8" cy="6.5" r="1.8" fill="var(--cream)"/></svg>
          Address - PO box 648, Brookvale NJ 07412
        </li>
      </ul>
    </div>
  </section>
</body>
</html>
```